Simple Reminder/Todo List Android App Design

This design project is to create a simple and straightforward design for a Reminder/Todo List Android app called Vessa Chore.

This Google Doc have more info
https://files.quillnest.net/doc/d/8kR_Q471bWt93mLpXvZ55Hc02JdqPywRaeJkTfsBNqWx/edit?usp=sharing

Target Market(s)

Android App Users

Font styles to use
Serif

Requirements
Must have
• Task List, Add Task, Add Reminder, Add SubTasks
Nice to have
• App Icon, Splash Screen
Should not have
• Login

```html
<!DOCTYPE html>
<html lang="en">
<head>
<meta charset="utf-8">
<title>Vessa Chore — Mark as Done for Sub Task</title>
<link rel="stylesheet" href="https://fonts.googleapis.com/css2?family=DM+Sans:wght@400;500;700&family=Montserrat:wght@700&display=swap">
<style>
  :root {
    --brand: #6288e6;
    --headline: #5f86e4;
    --screen-bg: #f5f8fe;
    --ink: #1d2144;
    --ink-soft: #2d3150;
    --muted: #9a9db0;
    --done: #5fdd2a;
    --pending: #8a8a8a;
    --ring: #e5e4fa;
    --white: #ffffff;
  }
  * { box-sizing: border-box; margin: 0; padding: 0; }
  html, body { width: 1200px; height: 955px; overflow: hidden; background: var(--white); }
  body { position: relative; font-family: "DM Sans", sans-serif; }

  .rings { position: absolute; inset: 0; }

  .screen {
    position: absolute; left: 118px; top: 78px; width: 370px; height: 798px;
    background: var(--screen-bg); border-radius: 26px; overflow: hidden;
  }
  .app-bar {
    position: absolute; left: 0; top: 0; width: 100%; height: 123px;
    background: var(--brand); border-radius: 26px; color: var(--white);
  }
  .status-time { position: absolute; left: 32px; top: 16px; font-size: 13px; font-weight: 500; opacity: .9; }
  .status-icons { position: absolute; right: 16px; top: 17px; }
  .back { position: absolute; left: 35px; top: 63px; }
  .app-title { position: absolute; left: 0; right: 0; top: 62px; text-align: center; font-size: 18px; font-weight: 700; }

  .section-label { position: absolute; left: 37px; font-size: 14.5px; font-weight: 700; color: var(--ink); }
  .parent-label { top: 155px; }
  .sub-label { top: 310px; }

  .parent-card {
    position: absolute; left: 37px; top: 193px; width: 296px; height: 75px;
    background: var(--white); border-radius: 6px; border-left: 9px solid var(--brand);
    box-shadow: 0 6px 16px rgba(98,136,230,.14); padding: 13px 0 0 23px;
  }
  .parent-title { font-size: 16px; font-weight: 500; color: var(--ink-soft); }
  .parent-time { margin-top: 10px; font-size: 13px; color: var(--muted); }

  .subtasks { position: absolute; left: 37px; top: 351px; width: 296px; list-style: none; }
  .subtask { position: relative; height: 39px; font-size: 14px; color: var(--ink-soft); line-height: 22px; }
  .subtask.is-done .subtask-name { text-decoration: line-through; }
  .check { position: absolute; right: 0; top: 0; width: 21px; height: 21px; border-radius: 3px; background: var(--pending); }
  .is-done .check { background: var(--done); }
  .check svg { position: absolute; left: 5px; top: 6px; }

  .save {
    position: absolute; left: 36px; top: 715px; width: 297px; height: 52px;
    background: var(--brand); border-radius: 3px; color: var(--white);
    font-size: 18px; font-weight: 700; display: flex; align-items: center; justify-content: center;
  }

  .headline {
    position: absolute; left: 550px; top: 390px;
    font-family: "Montserrat", sans-serif; font-weight: 700; font-size: 93px;
    line-height: 101px; color: var(--headline); letter-spacing: -1px;
  }
</style>
</head>
<body>
  <svg class="rings" width="1200" height="955" viewBox="0 0 1200 955" aria-hidden="true">
    <g fill="none" stroke="var(--ring)" stroke-width="1.2">
      <circle cx="1200" cy="477" r="397"/>
      <circle cx="1200" cy="477" r="311"/>
      <circle cx="1200" cy="477" r="226"/>
    </g>
  </svg>

  <main class="screen">
    <header class="app-bar">
      <span class="status-time">9:41</span>
      <svg class="status-icons" width="48" height="11" viewBox="0 0 48 11" aria-hidden="true" fill="#fff">
        <rect x="0" y="7" width="2.5" height="3" rx=".5"/><rect x="4" y="5" width="2.5" height="5" rx=".5"/>
        <rect x="8" y="3" width="2.5" height="7" rx=".5"/><rect x="12" y="1" width="2.5" height="9" rx=".5"/>
        <path d="M24 10l-2-2.2a3 3 0 0 1 4 0zM19.5 5.6a6.5 6.5 0 0 1 9 0l-1.3 1.3a4.7 4.7 0 0 0-6.4 0zM17.3 3.4a9.6 9.6 0 0 1 13.4 0l-1.3 1.3a7.8 7.8 0 0 0-10.8 0z"/>
        <rect x="34" y="2" width="13" height="7" rx="2"/>
      </svg>
      <svg class="back" width="26" height="24" viewBox="0 0 26 24" aria-label="Back" role="img">
        <path d="M24 12H3M12 3l-9 9 9 9" fill="none" stroke="#fff" stroke-width="2.2" stroke-linecap="round" stroke-linejoin="round"/>
      </svg>
      <h1 class="app-title">Sub Task</h1>
    </header>

    <h2 class="section-label parent-label">Parent Task</h2>
    <div class="parent-card">
      <p class="parent-title">Create brief for client</p>
      <p class="parent-time">09:30 - 10:00 AM</p>
    </div>

    <h2 class="section-label sub-label">Sub Task</h2>
    <ul class="subtasks">
      <li class="subtask is-done"><span class="subtask-name">Brainstorming on Design UI</span>
        <span class="check"><svg width="11" height="9" viewBox="0 0 11 9"><path d="M1 4.5l3 3L10 1" fill="none" stroke="#fff" stroke-width="1.5"/></svg></span></li>
      <li class="subtask is-done"><span class="subtask-name">Create new App presentation</span>
        <span class="check"><svg width="11" height="9" viewBox="0 0 11 9"><path d="M1 4.5l3 3L10 1" fill="none" stroke="#fff" stroke-width="1.5"/></svg></span></li>
      <li class="subtask"><span class="subtask-name">Discussion with Development team</span>
        <span class="check"><svg width="11" height="9" viewBox="0 0 11 9"><path d="M1 4.5l3 3L10 1" fill="none" stroke="#fff" stroke-width="1.5"/></svg></span></li>
      <li class="subtask"><span class="subtask-name">Handover files</span>
        <span class="check"><svg width="11" height="9" viewBox="0 0 11 9"><path d="M1 4.5l3 3L10 1" fill="none" stroke="#fff" stroke-width="1.5"/></svg></span></li>
    </ul>

    <div class="save">Save</div>
  </main>

  <p class="headline">Mark as Done<br>for Sub Task</p>
</body>
</html>
```